Vellora - Quality health delivered at your door

Vellora offers home and Community Based Services for adults who wish to continue live independently in their communities. We increase accessibility to health care, reduce health care delivery gap, reduce mortality and morbidity, reduce health while promoting healthy living in the comfort of our patients communities or homes.

We provide on site services and deliver high quality healthcare at your door. Our experienced physicians coordinate care with our certified nurse practitioners and provide chronic care management, physical therapy, rehabilitation and medications management.

Target Market(s)

Older population living in independent living facilities

Industry/Entity Type

Health Care

Contact Information for Business Card

Vellora

Number of Pages Required

4 page

Font styles to use
Sans Serif

Colors

Designer to choose colors to be used in the design.

```html
<!DOCTYPE html>
<html lang="en">
<head>
<meta charset="utf-8">
<title>Vellora - Quality health delivered at your door</title>
<link rel="stylesheet" href="https://fonts.googleapis.com/css2?family=Open+Sans:wght@400;600;700&family=Philosopher:wght@400;700&family=Cinzel:wght@700&display=swap">
<style>
:root{
  --orange:#f7941d;
  --orange-dark:#e5830f;
  --olive:#7d9b2b;
  --ink:#2a2a2a;
  --text:#555;
  --muted:#888;
  --bar:#2b2b2b;
  --light:#f3f3f3;
  --white:#fff;
}
*{margin:0;padding:0;box-sizing:border-box}
html,body{width:1200px;height:2575px;overflow:hidden}
body{position:relative;background:var(--white);font-family:"Open Sans",Arial,sans-serif;color:var(--text)}
.abs{position:absolute}

/* top bar */
.topbar{left:0;top:0;width:1200px;height:46px;background:var(--white)}
.top-cta{left:113px;top:0;width:176px;height:46px;background:var(--bar);color:var(--white);font-size:13px;font-weight:600;display:flex;align-items:center;justify-content:center;text-transform:uppercase}
.social{display:flex;gap:16px}
.social span{width:18px;height:18px;border-radius:50%;background:var(--muted)}
.top-social{right:113px;top:14px}

/* header */
.header{left:0;top:46px;width:1200px;height:114px;background:var(--white);border-top:1px solid #eee}
.brand{left:113px;top:50px;width:110px;text-align:center}
.brand-mark{width:62px;height:62px;border-radius:50%;background:var(--orange);margin:0 auto 4px}
.brand-name{font-size:19px;font-weight:600;color:var(--ink);letter-spacing:.5px}
.nav{right:113px;top:90px;display:flex;gap:30px;font-size:12.5px;font-weight:700;color:var(--ink);text-transform:uppercase}

/* hero */
.hero{left:0;top:160px;width:1200px;height:515px;background:linear-gradient(120deg,#8a9a72 0%,#c9d6b0 35%,#e8ecdc 55%,#a9c36a 80%,#6f8d3a 100%)}
.hero-title{left:0;top:330px;width:1200px;text-align:center;font-family:"Cinzel",serif;font-size:56px;color:#2d3a1c}
.hero-sub{left:0;top:396px;width:1200px;text-align:center;font-size:26px;font-weight:600;color:#2d3a1c}
.btn{background:var(--olive);color:var(--white);font-size:15px;display:flex;align-items:center;justify-content:center;border-radius:2px}
.hero-btn{left:524px;top:470px;width:172px;height:46px}

/* services */
.service-band{left:0;top:675px;width:1200px;height:213px;background:var(--light)}
.service{top:592px;width:170px;height:170px;background:var(--orange);color:var(--white);display:flex;flex-direction:column;align-items:center;justify-content:center;gap:18px;font-size:13.5px;text-transform:uppercase;font-weight:600;box-shadow:0 2px 4px rgba(0,0,0,.15)}
.service-icon{width:52px;height:52px;border:3px solid var(--white);border-radius:50%}
.service-intro{left:200px;top:812px;width:800px;text-align:center;font-size:16px;font-weight:600;line-height:1.75;color:#666}

/* headings */
.section-title{left:0;width:1200px;text-align:center;font-family:"Philosopher",sans-serif;font-size:38px;color:var(--ink)}
.rule{left:565px;width:70px;height:3px;background:var(--orange)}

/* help */
.help-photo{left:113px;top:1025px;width:418px;height:332px;background:linear-gradient(135deg,#dde6ee,#b7c9d8 60%,#eef2f5)}
.help-copy{left:572px;top:1025px;width:613px;font-size:12.5px;line-height:2.2;color:var(--text)}
.help-btn{left:574px;top:1254px;width:172px;height:42px}

/* testimonials */
.testi-band{left:0;top:1416px;width:1200px;height:469px;background:var(--light)}
.avatar{width:90px;height:90px;border-radius:50%;border:4px solid var(--white);background:linear-gradient(135deg,#d9b8a0,#9c7a66);box-shadow:0 1px 4px rgba(0,0,0,.2)}
.quote-dot{width:34px;height:34px;border-radius:50%;background:var(--orange);color:var(--white);font-family:Georgia,serif;font-size:26px;display:flex;align-items:center;justify-content:center;line-height:1}
.testi-text{width:310px;text-align:center;font-size:12px;line-height:1.9;color:var(--ink)}
.testi-name{width:310px;text-align:center;font-size:12px;color:var(--orange)}

/* contact band */
.contact-band{left:0;top:1885px;width:1200px;height:167px;background:var(--orange)}
.contact-title{left:0;top:1921px;width:1200px;text-align:center;font-size:23px;font-weight:700;color:var(--white)}
.contact-btn{left:462px;top:1972px;width:172px;height:42px;background:var(--orange-dark);color:var(--white);font-size:14px;display:flex;align-items:center;justify-content:center;border-radius:3px}

/* work */
.work-photo{top:2191px;width:309px;height:173px;background:linear-gradient(135deg,#3b7ac4,#9fc3e6 55%,#e1e8f0)}
.work-title{top:2378px;font-size:13.5px;color:var(--ink)}
.work-meta{top:2402px;font-size:11px;color:var(--muted)}

/* footer */
.footer{left:0;top:2454px;width:1200px;height:121px;background:var(--bar)}
.footer-btn{left:113px;top:2493px;width:172px;height:46px}
.footer-social{left:516px;top:2500px}
.footer-social span{background:#ddd}
.copyright{left:0;top:2536px;width:1200px;text-align:center;font-size:11px;color:#ccc}
.footer-brand{left:925px;top:2466px;width:160px;text-align:center}
.footer-brand .brand-mark{width:50px;height:50px;background:#777}
.footer-brand .brand-name{color:var(--white);font-size:18px}
</style>
</head>
<body>

<div class="abs topbar"></div>
<div class="abs top-cta">Request a Housecall</div>
<div class="abs social top-social"><span></span><span></span><span></span><span></span><span></span></div>

<header class="abs header"></header>
<div class="abs brand">
  <div class="brand-mark"></div>
  <div class="brand-name">VELLORA</div>
</div>
<nav class="abs nav"><span>Home</span><span>About Us</span><span>Our Services</span><span>News &amp; Events</span><span>Contact Us</span><span>Blog</span></nav>

<section class="abs hero" role="img" aria-label="Smiling woman stretching her arms outdoors in a sunny green park"></section>
<h1 class="abs hero-title">VELLORA</h1>
<p class="abs hero-sub">We Provide On Site Services And Deliver High Quality Healthcare At Your Door</p>
<div class="abs btn hero-btn">Request a Housecall</div>

<div class="abs service-band"></div>
<div class="abs service" style="left:113px"><div class="service-icon" role="img" aria-label="Physical therapy icon"></div>Physical Therapy</div>
<div class="abs service" style="left:314px"><div class="service-icon" role="img" aria-label="Mental health icon"></div>Mental Health</div>
<div class="abs service" style="left:515px"><div class="service-icon" role="img" aria-label="Dental health icon"></div>Dental Health</div>
<div class="abs service" style="left:716px"><div class="service-icon" role="img" aria-label="Transportation icon"></div>Transportation</div>
<div class="abs service" style="left:917px">
  <svg width="52" height="52" viewBox="0 0 52 52"><circle cx="26" cy="26" r="23.5" fill="none" stroke="#fff" stroke-width="3"/><path d="M26 14v24M14 26h24" stroke="#fff" stroke-width="3"/></svg>
  View All
</div>
<p class="abs service-intro">Vellora offers home and Community Based Services for adults who wish to continue to live independently in the comfort of their communities.</p>

<h2 class="abs section-title" style="top:928px">How Can We Help You?</h2>
<div class="abs rule" style="top:982px"></div>
<div class="abs help-photo" role="img" aria-label="Smiling nurse in a white coat talking on the phone"></div>
<p class="abs help-copy">Our visiting physicians work hand in hand with certified nurse practitioners to bring complete care into your home. Every visit begins with a careful review of your health history, current medications and daily routine. From there we build a plan that fits the way you live. Chronic care management, physical therapy, rehabilitation and medication reviews all happen in the comfort of your own surroundings. Families stay informed after every appointment, and our coordinators are always ready to arrange the next visit. We believe good care should come to you, so you can keep living independently within the community you know and love.</p>
<div class="abs btn help-btn">Request a Housecall</div>

<div class="abs testi-band"></div>
<h2 class="abs section-title" style="top:1462px">How Can We Help You?</h2>
<div class="abs rule" style="top:1516px"></div>

<div class="abs quote-dot" style="left:248px;top:1556px">&ldquo;</div>
<div class="abs avatar" role="img" aria-label="Portrait of a customer" style="left:220px;top:1607px"></div>
<p class="abs testi-text" style="left:110px;top:1722px">The nurse who visits my mother is patient and kind. Having care arrive at our door has made every week calmer for the whole family, and her health is improving.</p>
<p class="abs testi-name" style="left:110px;top:1820px">Miss Customer Name</p>

<div class="abs quote-dot" style="left:583px;top:1556px">&ldquo;</div>
<div class="abs avatar" role="img" aria-label="Portrait of a customer" style="left:555px;top:1607px"></div>
<p class="abs testi-text" style="left:445px;top:1722px">After my surgery the therapy sessions at home helped me walk again. The team was always on time, friendly and clear about each step of my recovery plan.</p>
<p class="abs testi-name" style="left:445px;top:1820px">Miss Customer Name</p>

<div class="abs quote-dot" style="left:915px;top:1556px">&ldquo;</div>
<div class="abs avatar" role="img" aria-label="Portrait of a customer" style="left:887px;top:1607px"></div>
<p class="abs testi-text" style="left:777px;top:1722px">I no longer worry about my medications. The physician checks everything during each visit and explains it simply, so I can stay in the home I love.</p>
<p class="abs testi-name" style="left:777px;top:1820px">Miss Customer Name</p>

<section class="abs contact-band"></section>
<p class="abs contact-title">Please Contact Us To Schedule A Time For Your Visit.</p>
<div class="abs contact-btn">Contact Us</div>

<h2 class="abs section-title" style="top:2092px">Our Work</h2>
<div class="abs rule" style="top:2146px"></div>
<div class="abs work-photo" style="left:113px" role="img" aria-label="Health care students in blue scrubs at a training session"></div>
<div class="abs work-photo" style="left:445px" role="img" aria-label="Group practicing first aid during health care training"></div>
<div class="abs work-photo" style="left:780px;background:linear-gradient(135deg,#f0a24a,#e8e3dc 55%,#c4d3e0)" role="img" aria-label="Trainees learning resuscitation on a training mannequin"></div>
<p class="abs work-title" style="left:113px">Training for Health care</p>
<p class="abs work-meta" style="left:113px">News &amp; Events</p>
<p class="abs work-title" style="left:445px">Training for Health care</p>
<p class="abs work-meta" style="left:445px">News &amp; Events</p>
<p class="abs work-title" style="left:780px">Training for Health care</p>
<p class="abs work-meta" style="left:780px">News &amp; Events</p>

<footer class="abs footer"></footer>
<div class="abs btn footer-btn">Request a Housecall</div>
<div class="abs social footer-social"><span></span><span></span><span></span><span></span><span></span></div>
<p class="abs copyright">All Rights Reserved</p>
<div class="abs footer-brand">
  <div class="brand-mark"></div>
  <div class="brand-name">VELLORA</div>
</div>

</body>
</html>
```